Summer orchestra weekly camp poster BVPE youth orchestra

We are youth orchestra in Texas holds a summer program called: Bright Bow Seasonal Studio (It's for students ages 8-18 who play already play violin/viola/cello/bass in the North Dallas, Texas Area.

We have 2 posters already from Artmarket designers that we have already been using and now are looking for some new designs. (you can see our other two previously purchased designs on the art market website)

The main difference in our camp is that we meet weekly on Saturday for 2 months June and July (not a week or 2 long camp like most music camps). This makes us a better choice locally because you are playing every week for 2 months out if the summer and less likely to lose skills over the summer vacation months.

Poster size: 11" by 17" but needs to be convertible to 8.5 to 11 size as well AND most importantly be in editable format via either Word or Publisher so we can use it every summer and be able to change dates, cost or location as needed.

All the details are below, but on the poster we would need the website listed: www.marlowridgeyouthensemble.example and tell them to go to that website to apply online beginning April 1st

That's how we get business, they go to our website and apply and pay with coinvault. It also needs to say really big BVPE BRIGHT BOW SEASONAL STUDIO

April 1st is when we being accepting online applications (every year, so don't put a year) Also put: Camp is held on Saturdays in June and July with final concert, last Sunday in July

Also on the poster we need: Our goal is to keep young musicians playing over the summer –so don’t put your instrument away for the summer! Keep in shape by joining us for the Marlow Ridge Youth Ensemble’s summer program – Bright Bow Seasonal Studio! Tuition is $225, which covers June/July Saturday rehearsals and the performance fee for the BKMT Hall concert, last Sunday in July.

I know we can't get all the info below on it, but I put it on so you could better understand what we are doing.

We have a logo already, that we have the rights to - I need something that kids/teens will think is cool looking and music related....we are string instruments only (violin, viola, cello, bass) we also want it to look classy looking, not cheap
I included 2 copies of the logo in different color set

here's all the details from our website:
Bright Bow Seasonal Studio (June and July) - Tuition: $225
Somewhere it should stress that we are not like other camps because we are weekly for two months. (There's a better way to state that but I'm not sure what that is)

Rehearsals on Saturdays June &July with final concert on last Sunday in July @ BKH Hall

Our goal is to keep young musicians playing over the summer –so don’t put your instrument away for the summer! Keep in shape by joining us for the Marlow Ridge Youth Ensemble’s new summer program – Bright Bow Seasonal Studio!

Tuition is $225, which covers June/July Saturday rehearsals and the performance fee for the BKMT Hall concert.

No audition is necessary. Enrollment is limited to the first 50 students in each age category, depending on instrumentation needs, so don’t delay – enrollment online begins April 1st. Siblings will receive a $50 discount, after the first child's regular priced tuition.

Bright Bow I: Students entering grades 6 and below (3:00 – 4:20 P.M. )
Bright Bow II: Students grades entering 7 and 8 (4:30 – 6:00 P.M.)
Bright Bow III: Students entering grades 9-12 (6:15 – 7:45 P.M.)

Summer camp attendance policy is more lenient due to summer vacations. Please notify BVPE of summer absences as soon as your vacation/camp dates are known.
Updates

Here is a link to the previous contest we held on ArtMarket last year.

http://jobs.artmarket.example/job.aspx?id=384619

http://poster.artmarket.example/contest.aspx?id=384619

Also Rehearsals are held at Pemberton Fiddles in Allen, TX

I am working today at a music festival and cannot get on the computer or artmarket website until after 6 or 7 p.m. tonight.  So if you are not getting feedback during the day today, that is why.  I will give feedback to everyone when I get home later tonight.  Thank you all for your work!

Reason: Hi everyone, I judged a music contest all day today and really need some time to look over all the entries. I appreciate everyone's hard work and will make a decision within the next 2 days. I want to be able to provide feedback to everyone and give everyone enough time to submit their best work, so I am extending the deadline by 2 days. I will have to make a decision at the end very quickly as we need to do a huge mail out as soon as the contest is over. Thank you everyone, we really do appreciate everyone's efforts in making our new poster for Bright Seasonal Bow Studio!

Target Market(s)

Parents of string players age 8-18 in North Texas along with students themselves.

Industry/Entity Type

Business

Requirements
Must have
• something showing we are different than the ordinary summer music camp
our QR code which I will email to you if your poster is the winner

```html
<!DOCTYPE html>
<html lang="en">
<head>
<meta charset="utf-8">
<title>BVPE Bright Bow Seasonal Studio</title>
<link href="https://fonts.googleapis.com/css2?family=Carlito:ital,wght@0,400;0,700;1,400;1,700&family=Libre+Baskerville:ital,wght@1,400;1,700&display=swap" rel="stylesheet">
<style>
  :root {
    --wine: #8a2640;
    --magenta: #a3124a;
    --ink: #1c1c1c;
    --rule: #5a5a5a;
    --accent-red: #b2383e;
  }
  * { margin: 0; padding: 0; box-sizing: border-box; }
  html, body { width: 1200px; height: 777px; overflow: hidden; background: #fff; }
  .poster {
    position: relative; width: 1200px; height: 777px; overflow: hidden;
    font-family: "Carlito", "Calibri", sans-serif; color: var(--ink);
    background:
      radial-gradient(ellipse at 15% 10%, #a9dccb 0%, transparent 45%),
      radial-gradient(ellipse at 95% 45%, #fbf5c4 0%, transparent 45%),
      radial-gradient(ellipse at 5% 80%, #f6b8b8 0%, transparent 40%),
      linear-gradient(160deg, #d9e9dc 0%, #ece9dc 40%, #f2efd8 70%, #e6f1d5 100%);
  }
  .staff-art {
    position: absolute; left: 0; top: 560px; width: 1200px; height: 217px;
    background:
      radial-gradient(ellipse at 55% 60%, rgba(214, 140, 200, 0.55) 0%, transparent 40%),
      linear-gradient(170deg, rgba(140, 230, 220, 0.0) 0%, rgba(120, 220, 215, 0.55) 45%, rgba(150, 200, 240, 0.6) 100%);
  }
  .title-band { position: absolute; left: 0; top: 0; width: 688px; height: 190px; border-bottom: 3px solid var(--rule); }
  .title {
    position: absolute; left: 14px; font-family: "Libre Baskerville", serif; font-style: italic; font-weight: 700;
    font-size: 50px; letter-spacing: -1px; color: var(--wine); text-shadow: 3px 3px 0 #3a3a3a; white-space: nowrap;
  }
  .title.l1 { top: 18px; }
  .title.l2 { top: 102px; }
  .apply-box {
    position: absolute; left: 688px; top: 0; width: 512px; height: 246px;
    background: linear-gradient(180deg, rgba(238,238,238,0.95), rgba(226,226,224,0.9)); text-align: center;
  }
  .apply-head { margin-top: 12px; font-size: 45px; color: var(--magenta); letter-spacing: 1px; }
  .apply-note { margin: 6px auto 0; width: 500px; font-style: italic; font-size: 20px; line-height: 32px; }
  .apply-date { margin-top: 6px; font-size: 28px; }
  .apply-site { margin-top: 16px; font-size: 26px; font-weight: 700; text-shadow: 1px 1px 2px #888; white-space: nowrap; }
  .story {
    position: absolute; left: 26px; top: 215px; width: 289px; height: 370px; padding: 10px 14px 0 17px;
    background: linear-gradient(180deg, rgba(200,205,205,0.75), rgba(215,215,215,0.6));
    border: 1px solid #aaa; box-shadow: 3px 3px 6px rgba(0,0,0,0.3);
    font-size: 20px; line-height: 30px; text-align: justify;
  }
  .story p + p { margin-top: 14px; }
  .tuition { position: absolute; left: 772px; top: 266px; font-size: 45px; font-weight: 700; }
  .limit { position: absolute; right: 20px; top: 320px; font-size: 14px; font-style: italic; }
  .includes { position: absolute; left: 371px; top: 326px; font-size: 19px; line-height: 29px; }
  .includes .label { text-decoration: underline; margin-bottom: 6px; }
  .includes .venue { font-style: italic; padding-left: 13px; }
  .schedule { position: absolute; left: 340px; width: 820px; top: 458px; text-align: center; font-size: 29px; line-height: 42px; }
  .schedule em { font-weight: 700; }
  .perks { position: absolute; left: 760px; top: 568px; width: 420px; font-size: 19px; line-height: 29px; }
  .perks h2 { font-size: 19px; font-style: italic; font-weight: 700; margin-bottom: 4px; }
  .perks ul { list-style: none; }
  .perks li { position: relative; padding-left: 18px; text-align: justify; }
  .perks li + li { margin-top: 6px; }
  .perks li::before { content: "♪"; position: absolute; left: 0; top: 0; font-size: 16px; }
  .offers {
    position: absolute; left: 518px; top: 612px; transform: rotate(-24deg); transform-origin: left top;
    font-family: "Libre Baskerville", serif; font-style: italic; font-size: 16px; line-height: 34px; color: var(--accent-red); letter-spacing: 1px;
  }
  .offers span { display: block; }
  .offers .second { padding-left: 28px; }
  .brand-mark { position: absolute; left: 30px; top: 630px; display: flex; align-items: center; gap: 12px; }
  .brand-mark .dot { width: 26px; height: 26px; background: #7a7a7a; border-radius: 50%; }
  .brand-mark .name { font-size: 56px; color: #6a6a6a; }
  .footer { position: absolute; left: 375px; top: 743px; font-size: 15px; font-style: italic; }
  .footer strong { font-style: normal; font-weight: 700; margin-left: 6px; }
  .pay-badge {
    position: absolute; left: 1084px; top: 728px; width: 92px; height: 38px; border-radius: 5px;
    background: #f7f1e2; border: 1px solid #c7b890; text-align: center; font-size: 12px; line-height: 16px; padding-top: 3px; color: #2a3a6a;
  }
</style>
</head>
<body>
<div class="poster">
  <div class="staff-art" role="img" aria-label="Flowing musical staff lines with notes in turquoise and violet"></div>

  <header class="title-band">
    <h1 class="title l1">BVPE BRIGHT BOW</h1>
    <div class="title l2">SEASONAL STUDIO</div>
  </header>

  <section class="apply-box">
    <div class="apply-head">GO ONLINE TO APPLY</div>
    <p class="apply-note">Visit our site to apply and submit your application to secure your space<sup>*</sup></p>
    <p class="apply-date">Applications Open 1 April</p>
    <p class="apply-site">www.marlowridgeyouthensemble.example</p>
  </section>

  <section class="story">
    <p><b>Our goal</b> is to <b>keep young musicians playing</b> over the summer time; so don’t put your instrument away <b>this summer!</b></p>
    <p><b>Keep in shape</b> by joining us for the <b>Marlow Ridge Youth Ensemble’s</b> New Summer Program: <b><i>Bright Bow Seasonal Studio</i></b></p>
  </section>

  <div class="tuition">TUITION FEE : $225</div>
  <div class="limit">*Limited to 50 Entrants Per Age category</div>

  <section class="includes">
    <p class="label">Fee Includes :-</p>
    <p>All rehearsals PLUS Performance Fee</p>
    <p class="venue">(BKMT Hall Concert - Last Sunday of July)</p>
  </section>

  <p class="schedule"><em>Bright Bow Seasonal Studio</em> is taking place Saturdays during June &amp; July with a Final Concert held on the last Sunday in July.</p>

  <section class="perks">
    <h2>We Are Different To The Rest</h2>
    <ul>
      <li>Runs on Saturdays for a period of <b>2 months;</b></li>
      <li>Opportunity to <b>play every week</b> for a <b>full 2 months</b> over summer vacation time;</li>
      <li>Keep skills in practice</li>
    </ul>
  </section>

  <div class="offers">
    <span>No Auditions Necessary</span>
    <span class="second">Siblings get $ 50 off</span>
  </div>

  <div class="brand-mark"><span class="dot"></span><span class="name">BVPE</span></div>

  <p class="footer">For more information, rehearsal times and online applications <strong>www.marlowridgeyouthensemble.example</strong></p>

  <div class="pay-badge">Pay with<br>CoinVault</div>
</div>
</body>
</html>
```